Robotic startup business cards

We are looking for a design for a set of business cards which reflect the spirit and humor of Torvexa Robotics. We want to present ourselves as sleek, professional, but laid-back consulting company.

We primarily focus on developing robotic arms software. This software controls robots and does things like grab items, pick objects up, move them, etc.

We want to allow you maximum design creativity, but do ask that you consider our existing style guidelines (see attached files) in order to make our brand cohesive.

Target Market(s)

Startups and Mid-size robotic companies

Industry/Entity Type

Business

Contact Information for Business Card

Liam Brantly, PhD
Roboticist | Torvexa Consulting | 318.572.6094

Font styles to use
Other font styles liked:
• Source code pro

Requirements
Must have
• robots or robotic arms
• similar color scheme that works with existing brand guidelines
Nice to have
• please consider our existing style guidelines (see attached files) in order to make our brand cohesive.
• minimalism style is generally nice.
Should not have
• An old, boring, or corporate feel. Too much text.

```html
<!DOCTYPE html>
<html lang="en">
<head>
<meta charset="utf-8">
<title>Torvexa Robotics – Business Cards</title>
<link rel="stylesheet" href="https://fonts.googleapis.com/css2?family=Source+Code+Pro:wght@400&family=Source+Sans+3:wght@400&display=swap">
<style>
  :root {
    --backdrop: #b9b9b9;
    --card-top: #05d293;
    --card-bottom: #00bf86;
    --ink: #263630;
    --ink-soft: #2c3d36;
  }
  * { margin: 0; padding: 0; box-sizing: border-box; }
  html, body {
    width: 1200px;
    height: 576px;
    overflow: hidden;
    background: var(--backdrop);
  }
  .canvas {
    position: relative;
    width: 1200px;
    height: 576px;
  }
  .card {
    position: absolute;
    width: 485px;
    height: 292px;
    border-radius: 16px;
    background: linear-gradient(180deg, var(--card-top) 0%, var(--card-top) 55%, var(--card-bottom) 100%);
    color: var(--ink);
    font-family: "Source Sans 3", "Source Sans Pro", sans-serif;
  }
  .card--front { left: 82px; top: 139px; }
  .card--back { left: 602px; top: 138px; }

  .holder-name {
    position: absolute;
    left: 36px;
    top: 36px;
    font-size: 21px;
    font-weight: 400;
    line-height: 1;
    letter-spacing: 0.1px;
  }
  .holder-role {
    position: absolute;
    left: 36px;
    top: 66px;
    font-size: 12px;
    line-height: 1;
    color: var(--ink-soft);
  }
  .contact-list {
    position: absolute;
    left: 36px;
    top: 97px;
    list-style: none;
    font-size: 12px;
    line-height: 16.5px;
    color: var(--ink-soft);
  }

  .brand {
    position: absolute;
    display: flex;
    align-items: center;
    gap: 12px;
    top: 215px;
    height: 30px;
  }
  .card--front .brand { left: 36px; }
  .card--back .brand { right: 34px; }
  .brand-square {
    width: 14px;
    height: 14px;
    background: var(--ink);
  }
  .brand-name {
    font-family: "Source Code Pro", monospace;
    font-size: 22px;
    font-weight: 400;
    letter-spacing: 4px;
    line-height: 1;
    color: var(--ink);
  }
</style>
</head>
<body>
  <main class="canvas">
    <section class="card card--front" aria-label="Business card front">
      <h1 class="holder-name">Liam Brantly, PhD</h1>
      <p class="holder-role">Roboticist | Torvexa Consulting</p>
      <ul class="contact-list">
        <li>318.572.6094</li>
        <li>liam@torvexa.com</li>
        <li>www.torvexa.com</li>
      </ul>
      <div class="brand">
        <span class="brand-square" aria-hidden="true"></span>
        <span class="brand-name">TORVEXA</span>
      </div>
    </section>

    <section class="card card--back" aria-label="Business card back">
      <div class="brand">
        <span class="brand-square" aria-hidden="true"></span>
        <span class="brand-name">TORVEXA</span>
      </div>
    </section>
  </main>
</body>
</html>
```